Mortgage Broking Business needs a 1 page single sided 'brochure / flyer

I require a one page single sided 'brochure / flyer' that i can 1. Email to potential clients (Limited MB so easily emailed) and 2. Print and post to potential clients. (A4) High resolution color. I think both should be Landscape format.
Look at my website www.brightvalemortgages.com.au to find inspiration - clear / clean / crisp / blue tones

Target Market(s)

Potential borrowers - age 25 to 50 for home and Investment Loans

Industry/Entity Type

Finance

Font styles to use
Sans Serif

Colors
33a6d7
0692cd

Requirements
Must have
• Must Include:
• -My Headshot
• -Company Logo
• -Lenders Logos - can cut and paste from my affiliate website http://www.harbourlinkfinance.com.au/index.php?page=preferredpartners
• - Tag Line - Smart Lending Solutions Sydney Australia
• - Service Offering
Nice to have
• Lightbulb as per website
Should not have
• Should not look cluttered

```html
<!DOCTYPE html>
<html lang="en">
<head>
<meta charset="utf-8">
<title>Brightvale Mortgages – Flyer</title>
<link rel="stylesheet" href="https://fonts.googleapis.com/css2?family=Source+Sans+3:ital,wght@0,300;0,400;0,600;1,400&family=Roboto+Condensed:ital,wght@0,400;0,700;1,700&display=swap">
<style>
  :root {
    --blue: #33a6d7;
    --blue-deep: #0692cd;
    --blue-light: #8fd3f0;
    --text-grey: #5a5a5a;
    --logo-grey: #8a8d90;
    --paper: #ffffff;
  }
  * { box-sizing: border-box; margin: 0; padding: 0; }
  html, body { width: 1200px; height: 851px; overflow: hidden; background: var(--paper); }
  .flyer { position: relative; width: 1200px; height: 851px; font-family: "Source Sans 3", sans-serif; color: var(--text-grey); }

  .hero {
    position: absolute; left: 13px; top: 19px; width: 1166px; height: 367px;
    background: linear-gradient(90deg, var(--blue) 0%, #3aaadb 55%, #5cbde6 100%);
    overflow: hidden;
  }
  .hero__glow {
    position: absolute; right: -40px; top: -40px; width: 520px; height: 460px;
    background: radial-gradient(circle at 55% 45%, #e9f7fd 0%, #b3e1f5 25%, rgba(92,189,230,0) 65%);
  }
  .hero__bulb {
    position: absolute; left: 800px; top: 12px; width: 270px; height: 350px;
    background: radial-gradient(ellipse at 50% 35%, #dff3fc 0%, #9ed8f1 45%, #5fb9e0 80%);
    border-radius: 50% 50% 40% 40% / 45% 45% 55% 55%;
    opacity: .85;
  }
  .hero__headline {
    position: absolute; left: 53px; top: 88px; width: 640px;
    color: #fff; font-weight: 400; font-size: 42px; line-height: 52px; letter-spacing: -0.6px;
  }
  .hero__headline em { font-style: italic; }

  .brand-card {
    position: absolute; left: 58px; top: 292px; width: 307px; height: 121px;
    background: #fff; box-shadow: 0 2px 6px rgba(0,0,0,.25);
  }
  .brand-card__name {
    position: absolute; left: 20px; top: 24px;
    font-size: 30px; font-weight: 600; letter-spacing: 0.5px; color: var(--blue); line-height: 1;
  }
  .brand-card__mark {
    position: absolute; left: 264px; top: 27px; width: 24px; height: 24px; background: var(--blue-light);
  }
  .brand-card__tagline {
    position: absolute; left: 14px; top: 88px; font-size: 15.5px; font-weight: 400; color: var(--blue-light); white-space: nowrap;
  }
  .brand-card__tagline span { color: var(--logo-grey); }

  .services {
    position: absolute; left: 59px; top: 425px; width: 307px; height: 213px;
    background: #fff; box-shadow: 0 2px 6px rgba(0,0,0,.25); padding: 8px 10px 0 9px;
  }
  .services__title {
    font-family: "Roboto Condensed", sans-serif; font-weight: 400; font-size: 19px; color: var(--blue-deep); letter-spacing: -0.3px;
  }
  .services__list { list-style: none; margin: 14px 0 0 26px; }
  .services__list li { position: relative; font-size: 16px; line-height: 23px; margin-bottom: 7px; padding-left: 0; }
  .services__list li::before {
    content: ""; position: absolute; left: -16px; top: 9px; width: 6px; height: 6px; border-radius: 50%; background: var(--blue);
  }
  .services__list .indent { padding-left: 10px; }

  .lenders { position: absolute; left: 50px; top: 680px; width: 356px; display: grid; grid-template-columns: repeat(12, 24px); column-gap: 6px; row-gap: 18px; }
  .lender-badge { height: 9px; border-radius: 2px; background: #c9d3da; }
  .lender-badge--blue { background: #9bc8e2; }
  .lender-badge--red { background: #e0a3a3; }

  .call-box {
    position: absolute; left: 486px; top: 416px; width: 308px; height: 257px; background: var(--blue);
    color: #fff;
  }
  .call-box__heading {
    position: absolute; left: 0; top: 19px; width: 100%; text-align: center;
    font-family: "Roboto Condensed", sans-serif; font-weight: 700; font-size: 23px; line-height: 31px; letter-spacing: -0.3px;
  }
  .call-box__heading em { font-style: italic; }
  .contact {
    position: absolute; left: 150px; top: 119px; width: 158px; text-align: center;
    font-family: "Roboto Condensed", sans-serif; font-size: 14.5px; line-height: 21.5px; text-transform: uppercase;
  }
  .headshot {
    position: absolute; left: 476px; top: 499px; width: 154px; height: 231px;
    background: linear-gradient(180deg, #8f8579 0%, #b39d8a 40%, #e9b9c4 75%, #f2c9d2 100%);
    box-shadow: 0 2px 6px rgba(0,0,0,.3);
  }
  .disclosure { position: absolute; left: 474px; top: 775px; font-size: 11px; line-height: 14.5px; color: var(--blue-deep); }

  .profile { position: absolute; left: 860px; top: 413px; width: 300px; }
  .profile__heading {
    font-family: "Roboto Condensed", sans-serif; font-weight: 400; font-size: 20px; color: var(--blue-deep); letter-spacing: -0.3px;
  }
  .profile__text { margin-top: 6px; font-size: 16px; line-height: 25.6px; }
  .profile__heading--edu { margin-top: 10px; }
  .profile__list { list-style: none; margin: 6px 0 0 26px; font-size: 16px; line-height: 25.6px; }
  .profile__list li::before { content: "• "; }
</style>
</head>
<body>
<main class="flyer">
  <section class="hero">
    <div class="hero__glow"></div>
    <div class="hero__bulb" role="img" aria-label="Glowing light bulb photograph in pale blue tones"></div>
    <h1 class="hero__headline">With over <em>40 Lenders</em> and <em>Preferred Partners</em> on our Panel, we can find a solution for <em>you</em>.</h1>
  </section>

  <div class="brand-card">
    <div class="brand-card__name">BRIGHTVALE</div>
    <div class="brand-card__mark"></div>
    <div class="brand-card__tagline">Smart Lending Solutions <span>Sydney Australia</span></div>
  </div>

  <section class="services">
    <h2 class="services__title">Call us for all of your borrowing needs:</h2>
    <ul class="services__list">
      <li>Refinance of existing loans to lower<br><span class="indent">Interest rates</span></li>
      <li>Top Ups for renovations</li>
      <li>Purchase of Owner Occupied and<br><span class="indent">Investment Property</span></li>
      <li>Purchase of Commercial Property</li>
    </ul>
  </section>

  <div class="lenders" aria-label="Panel lenders">
    <span class="lender-badge lender-badge--blue"></span><span class="lender-badge"></span><span class="lender-badge"></span><span class="lender-badge"></span><span class="lender-badge"></span><span class="lender-badge"></span><span class="lender-badge lender-badge--blue"></span><span class="lender-badge"></span><span class="lender-badge"></span><span class="lender-badge"></span><span class="lender-badge"></span><span class="lender-badge"></span>
    <span class="lender-badge lender-badge--red"></span><span class="lender-badge"></span><span class="lender-badge lender-badge--blue"></span><span class="lender-badge"></span><span class="lender-badge"></span><span class="lender-badge lender-badge--blue"></span><span class="lender-badge lender-badge--blue"></span><span class="lender-badge"></span><span class="lender-badge"></span><span class="lender-badge"></span><span class="lender-badge lender-badge--blue"></span><span class="lender-badge"></span>
    <span class="lender-badge lender-badge--red"></span><span class="lender-badge"></span><span class="lender-badge"></span><span class="lender-badge"></span><span class="lender-badge"></span><span class="lender-badge"></span><span class="lender-badge lender-badge--blue"></span><span class="lender-badge"></span><span class="lender-badge"></span><span class="lender-badge"></span><span class="lender-badge lender-badge--red"></span><span class="lender-badge"></span>
    <span class="lender-badge lender-badge--red"></span><span class="lender-badge"></span><span class="lender-badge lender-badge--red"></span><span class="lender-badge"></span><span class="lender-badge"></span><span class="lender-badge"></span><span class="lender-badge"></span><span class="lender-badge lender-badge--blue"></span><span class="lender-badge lender-badge--blue"></span><span class="lender-badge"></span><span class="lender-badge"></span><span class="lender-badge"></span>
    <span class="lender-badge lender-badge--red"></span><span class="lender-badge lender-badge--blue"></span><span class="lender-badge"></span><span class="lender-badge lender-badge--blue"></span><span class="lender-badge"></span><span class="lender-badge"></span><span class="lender-badge"></span><span class="lender-badge"></span><span class="lender-badge"></span><span class="lender-badge"></span><span class="lender-badge"></span><span class="lender-badge"></span>
  </div>

  <section class="call-box">
    <h2 class="call-box__heading">Call Mark <em>now</em> to discuss your<br>borrowing needs.</h2>
    <address class="contact" style="font-style:normal">
      Contact:<br>Mark Ellery-Dunn<br>0412 555 301<br>PO Box 318<br>Harbour Point NSW 2190
    </address>
  </section>
  <div class="headshot" role="img" aria-label="Headshot of the broker in a pink checked shirt"></div>

  <p class="disclosure">Disclosure:<br>Brightvale Financial Services Pty Ltd<br>T/As Brightvale Mortgages<br>Australian Credit Licence No: 412736</p>

  <section class="profile">
    <h2 class="profile__heading">EXPERIENCE:</h2>
    <p class="profile__text">Mark Ellery-Dunn has been working in the Finance Industry for over 20 years. With a background in Accounting, Banking, Financial Planning and Mortgage Broking Mark brings a wealth of knowledge and experience to assist with all of your Finance needs.</p>
    <h2 class="profile__heading profile__heading--edu">EDUCATION / QUALIFICATIONS</h2>
    <ul class="profile__list">
      <li>BComm Eastbridge University</li>
      <li>Dip Financial Planning</li>
      <li>Cert IV Mortgage Broking</li>
      <li>Justice of the Peace</li>
      <li>Member MBAN / FPN Affiliate</li>
    </ul>
  </section>
</main>
</body>
</html>
```